International Consultancy Needs Slick Professional Presentation Graphic

Quarvel are an international engineering and advisory consultancy servicing the mining industry with a mix of Technology (Software), Services (consulting) and Systems (work structures).

We need a slick presentation graphic for use in presentation slides, whitepapers. I have attached a basic pic of the information we want to convey. Flat or 3D no preference, colouring no preference. Don't have to be circles, that was just easiest to draft up initially.

Industry/Entity Type

Mining

```html
<!DOCTYPE html>
<html lang="en">
<head>
<meta charset="utf-8">
<title>Capability Model</title>
<link href="https://fonts.googleapis.com/css2?family=Arimo:wght@400;700&display=swap" rel="stylesheet">
<style>
  :root {
    --page-bg: #ffffff;
    --frame: #c9c9c9;
    --ink: #111111;
    --label: #ffffff;
    --systems: #ffc20e;
    --technology: #1cc3c6;
    --people: #f516de;
    --systems-technology: #129a1e;
    --systems-people: #ef1a1a;
    --technology-people: #0b12b3;
    --core: #ffffff;
  }
  html, body {
    margin: 0;
    padding: 0;
    overflow: hidden;
    background: var(--page-bg);
  }
  .slide {
    position: relative;
    width: 1200px;
    height: 846px;
    background: var(--page-bg);
    font-family: "Arimo", Arial, sans-serif;
    overflow: hidden;
  }
  .slide-frame {
    position: absolute;
    left: 30px;
    top: 24px;
    width: 1138px;
    height: 794px;
    border: 2px solid var(--frame);
    box-sizing: border-box;
  }
  .slide-heading {
    position: absolute;
    left: 56px;
    top: 52px;
    color: var(--ink);
  }
  .slide-title {
    margin: 0;
    font-size: 34px;
    font-weight: 700;
    line-height: 1;
  }
  .slide-subtitle {
    margin: 6px 0 0;
    font-size: 30px;
    font-weight: 400;
    line-height: 1;
  }
  .venn {
    position: absolute;
    left: 0;
    top: 0;
  }
  .venn-label {
    fill: var(--label);
    font-family: "Arimo", Arial, sans-serif;
    font-weight: 700;
    font-size: 31px;
    text-anchor: middle;
  }
  .overlap-label {
    fill: var(--label);
    font-family: "Arimo", Arial, sans-serif;
    font-weight: 400;
    font-size: 21px;
    text-anchor: middle;
  }
  .core-label {
    fill: var(--ink);
    font-family: "Arimo", Arial, sans-serif;
    font-weight: 700;
    font-size: 25px;
    text-anchor: middle;
  }
  .icon { fill: var(--label); }
  .icon-line { fill: none; stroke: var(--label); stroke-width: 4; stroke-linecap: round; }
  .icon-cut { fill: none; stroke: var(--systems); stroke-width: 3; }
  .icon-cut-tech { fill: none; stroke: var(--technology); stroke-width: 3; stroke-linecap: round; }
</style>
</head>
<body>
<main class="slide">
  <div class="slide-frame"></div>

  <header class="slide-heading">
    <h1 class="slide-title">TITLE GOES HERE</h1>
    <p class="slide-subtitle">Subtitle Goes Here</p>
  </header>

  <svg class="venn" width="1200" height="846" viewBox="0 0 1200 846" role="img" aria-label="Capability sits where Systems, Technology and People overlap">
    <defs>
      <clipPath id="clip-systems"><circle cx="600" cy="312" r="210"/></clipPath>
      <clipPath id="clip-technology"><circle cx="468" cy="560" r="212"/></clipPath>
      <clipPath id="clip-people"><circle cx="732" cy="560" r="212"/></clipPath>
      <radialGradient id="sheen" cx="50%" cy="40%" r="60%">
        <stop offset="0%" stop-color="#ffffff" stop-opacity="0.12"/>
        <stop offset="100%" stop-color="#000000" stop-opacity="0.08"/>
      </radialGradient>
      <filter id="soft-shadow" x="-20%" y="-20%" width="140%" height="140%">
        <feDropShadow dx="0" dy="4" stdDeviation="6" flood-color="#000" flood-opacity="0.25"/>
      </filter>
    </defs>

    <!-- Main circles -->
    <g class="circles" filter="url(#soft-shadow)">
      <circle cx="600" cy="312" r="210" fill="var(--systems)"/>
      <circle cx="468" cy="560" r="212" fill="var(--technology)"/>
      <circle cx="732" cy="560" r="212" fill="var(--people)"/>
    </g>

    <!-- Pairwise overlaps -->
    <g clip-path="url(#clip-systems)">
      <circle cx="468" cy="560" r="212" fill="var(--systems-technology)"/>
      <circle cx="732" cy="560" r="212" fill="var(--systems-people)"/>
    </g>
    <g clip-path="url(#clip-technology)">
      <circle cx="732" cy="560" r="212" fill="var(--technology-people)"/>
    </g>

    <!-- Core overlap -->
    <g clip-path="url(#clip-systems)">
      <g clip-path="url(#clip-technology)">
        <circle cx="732" cy="560" r="212" fill="var(--core)"/>
      </g>
    </g>

    <!-- Subtle sheen -->
    <circle cx="600" cy="312" r="210" fill="url(#sheen)"/>
    <circle cx="468" cy="560" r="212" fill="url(#sheen)"/>
    <circle cx="732" cy="560" r="212" fill="url(#sheen)"/>

    <!-- Systems icon: server with monitor -->
    <g class="icon-systems" transform="translate(568,172)">
      <rect class="icon" x="0" y="0" width="38" height="54" rx="3"/>
      <line class="icon-cut" x1="6" y1="12" x2="32" y2="12"/>
      <line class="icon-cut" x1="6" y1="22" x2="32" y2="22"/>
      <line class="icon-cut" x1="6" y1="32" x2="32" y2="32"/>
      <rect class="icon" x="30" y="26" width="38" height="26" rx="3" stroke="var(--systems)" stroke-width="3"/>
      <rect class="icon" x="43" y="52" width="12" height="8"/>
      <rect class="icon" x="36" y="59" width="26" height="4"/>
      <path class="icon-line" d="M44 8 q14 0 14 12" stroke-width="3"/>
      <path class="icon" d="M52 18 l6 8 l6 -8 z"/>
    </g>
    <text class="venn-label" x="600" y="282">SYSTEMS</text>

    <!-- Technology icon: circuit sheet -->
    <g class="icon-technology" transform="translate(362,490)">
      <path class="icon" d="M0 0 h40 l16 16 v48 h-56 z"/>
      <circle class="icon-cut-tech" cx="14" cy="20" r="4"/>
      <circle class="icon-cut-tech" cx="40" cy="36" r="4"/>
      <circle class="icon-cut-tech" cx="16" cy="50" r="4"/>
      <path class="icon-cut-tech" d="M18 20 h10 v16 h8 M20 50 h12 v-10"/>
    </g>
    <text class="venn-label" x="394" y="608">TECHNOLOGY</text>

    <!-- People icon: group silhouettes -->
    <g class="icon-people" transform="translate(772,500)">
      <circle class="icon" cx="14" cy="16" r="10"/>
      <path class="icon" d="M0 52 v-10 q0 -14 14 -14 q14 0 14 14 v10 z"/>
      <circle class="icon" cx="62" cy="16" r="10"/>
      <path class="icon" d="M48 52 v-10 q0 -14 14 -14 q14 0 14 14 v10 z"/>
      <circle class="icon" cx="38" cy="12" r="13" stroke="var(--people)" stroke-width="3"/>
      <path class="icon" d="M20 58 v-12 q0 -18 18 -18 q18 0 18 18 v12 z" stroke="var(--people)" stroke-width="3"/>
    </g>
    <text class="venn-label" x="810" y="608">PEOPLE</text>

    <!-- Overlap labels -->
    <text class="overlap-label" x="494" y="380">
      <tspan x="494">System</tspan>
      <tspan x="494" dy="25">Interface</tspan>
      <tspan x="494" dy="25">Engineering</tspan>
    </text>
    <text class="overlap-label" x="696" y="392">
      <tspan x="696">Organisation</tspan>
      <tspan x="696" dy="25">Design</tspan>
    </text>
    <text class="overlap-label" x="600" y="562">
      <tspan x="600">User</tspan>
      <tspan x="600" dy="25">Interface</tspan>
      <tspan x="600" dy="25">Engineering</tspan>
    </text>

    <text class="core-label" x="602" y="476">Capability</text>
  </svg>
</main>
</body>
</html>
```